we can communicate on this, but i want to follow the approach we took on Pell|Quorn & Tillet but i feel the card front needs the black background and the platinum and gold logo. The back? I am open. we can use the same info from PQ&T. Vellum Crest is an enhanced equity investment fund - basically a very exclusive boutique hedge fund that uses only stock options. very advanced things. hope you are interested

Contact Information for Business Card

Dr. Owen T. Brisket, CFA
Scientifique de fusée financière
555.014.2296
TheDoc4793@mailvessel.example

4718 Fennel Brook Way N.
West Fargo, ND 58078

No web site

Colors

Designer to choose colors to be used in the design.

Requirements
Nice to have
• I tend to prefer the most visible applications of the logo to include logo and name, the logo version with a black background and the gold and platinum components separated by the black. I see this working well for a single side (logo and name - this is card front to me).
• I am fairly open to other treatments on the reverse side with the data. To me, it makes sense to have a different color rendition of the logo on the reverse and it may be a muted black tone on tone or an oversized portion that would have spot UV. Or, the reverse may play with colors and layout
Should not have
• Other colors = no no
• Decorative font

```html
<!DOCTYPE html>
<html lang="en">
<head>
<meta charset="utf-8">
<title>Vellum Crest – Business Card</title>
<link rel="stylesheet" href="https://fonts.googleapis.com/css2?family=Josefin+Sans:wght@400;600;700&display=swap">
<style>
  :root {
    --backdrop: #6d6d6d;
    --card-black: #050505;
    --gold: #c6b152;
    --gold-light: #d9c86a;
    --platinum: #e6e6e6;
    --ink: #111111;
  }
  * { box-sizing: border-box; margin: 0; padding: 0; }
  html, body {
    width: 1200px; height: 800px; overflow: hidden;
    background: var(--backdrop);
    font-family: "Josefin Sans", sans-serif;
  }
  .canvas {
    width: 1200px; height: 800px;
    display: flex; flex-direction: column;
    align-items: center; justify-content: center; gap: 36px;
  }
  .card {
    position: relative;
    width: 620px; height: 354px;
    background: var(--card-black);
    overflow: hidden;
    box-shadow: 0 10px 28px rgba(0,0,0,.35);
  }

  /* Contact side */
  .card-waves { position: absolute; inset: 0; }
  .brand-small {
    position: absolute; left: 42px; top: 30px;
    display: flex; flex-direction: column; align-items: center; gap: 10px;
  }
  .brand-dot {
    width: 44px; height: 44px; border-radius: 50%;
    background: var(--gold);
  }
  .brand-name-small {
    color: var(--platinum);
    font-weight: 700; font-size: 14px; letter-spacing: 1.5px;
    text-transform: uppercase;
  }
  .holder {
    position: absolute; right: 44px; top: 38px; text-align: right;
  }
  .holder-name {
    color: var(--gold);
    font-weight: 700; font-size: 20px; letter-spacing: 1.2px;
    text-transform: uppercase; white-space: nowrap;
  }
  .holder-role {
    color: var(--platinum);
    font-weight: 400; font-size: 15px; letter-spacing: .8px;
    margin-top: 4px;
  }
  .contact-list {
    position: absolute; left: 40px; right: 30px; top: 256px;
    display: grid; grid-template-columns: 1.15fr 1fr; row-gap: 14px; column-gap: 20px;
    align-items: center;
    list-style: none;
  }
  .contact-item {
    display: flex; align-items: center; gap: 12px;
    color: var(--ink); font-size: 12.5px; letter-spacing: .4px; line-height: 1.35;
  }
  .contact-icon { width: 22px; height: 22px; flex: none; }

  /* Logo side */
  .card-logo-side {
    display: flex; flex-direction: column; align-items: center; justify-content: center; gap: 22px;
  }
  .brand-dot-large {
    width: 110px; height: 110px; border-radius: 50%;
    background: var(--gold);
  }
  .brand-name-large {
    color: var(--platinum);
    font-weight: 700; font-size: 40px; letter-spacing: 3px;
    text-transform: uppercase;
  }
</style>
</head>
<body>
<main class="canvas">

  <section class="card card-contact-side">
    <svg class="card-waves" viewBox="0 0 620 354" preserveAspectRatio="none" aria-hidden="true">
      <defs>
        <radialGradient id="goldGlow" cx="0.35" cy="0.3" r="0.85">
          <stop offset="0" stop-color="#d6c466"/>
          <stop offset="0.55" stop-color="#a8963c"/>
          <stop offset="1" stop-color="#4d4416"/>
        </radialGradient>
      </defs>
      <path d="M0 208 C110 192 210 232 330 208 C440 186 540 190 620 200 L620 354 L0 354 Z" fill="#3f3812"/>
      <path d="M0 222 C100 236 210 190 340 212 C440 230 530 212 620 220 L620 354 L0 354 Z" fill="#7d6e2a" opacity="0.85"/>
      <path d="M0 236 C140 212 250 240 380 232 C480 226 560 240 620 236 L620 354 L0 354 Z" fill="#a08e38" opacity="0.8"/>
      <path d="M0 248 C150 232 260 254 390 244 C490 236 560 248 620 244 L620 354 L0 354 Z" fill="url(#goldGlow)"/>
    </svg>

    <div class="brand-small">
      <span class="brand-dot"></span>
      <span class="brand-name-small">Vellum Crest</span>
    </div>

    <div class="holder">
      <p class="holder-name">Dr. Owen T. Brisket, CFA</p>
      <p class="holder-role">Scientifique de fusée financière</p>
    </div>

    <ul class="contact-list">
      <li class="contact-item">
        <svg class="contact-icon" viewBox="0 0 22 22" aria-hidden="true">
          <circle cx="11" cy="11" r="11" fill="var(--ink)"/>
          <path d="M11 5.5a3.6 3.6 0 0 0-3.6 3.6c0 2.7 3.6 7 3.6 7s3.6-4.3 3.6-7A3.6 3.6 0 0 0 11 5.5z" fill="var(--gold-light)"/>
          <circle cx="11" cy="9.1" r="1.3" fill="var(--ink)"/>
        </svg>
        <span>4718 Fennel Brook Way N.<br>West Fargo, ND 58078</span>
      </li>
      <li class="contact-item">
        <svg class="contact-icon" viewBox="0 0 22 22" aria-hidden="true">
          <circle cx="11" cy="11" r="11" fill="var(--ink)"/>
          <path d="M7.6 6.2l1.9-.4 1.1 2.6-1.2 1c.6 1.3 1.6 2.3 2.9 2.9l1-1.2 2.6 1.1-.4 1.9c-.1.4-.5.7-.9.7C10.3 14.8 7 11.5 6.9 7.1c0-.4.3-.8.7-.9z" fill="var(--gold-light)"/>
        </svg>
        <span>555.014.2296</span>
      </li>
      <li class="contact-item">
        <svg class="contact-icon" viewBox="0 0 22 22" aria-hidden="true">
          <circle cx="11" cy="11" r="11" fill="var(--ink)"/>
          <rect x="6" y="7.5" width="10" height="7" rx="0.8" fill="var(--gold-light)"/>
          <path d="M6.3 7.9L11 11.6l4.7-3.7" fill="none" stroke="var(--ink)" stroke-width="0.9"/>
        </svg>
        <span>TheDoc4793@mailvessel.example</span>
      </li>
    </ul>
  </section>

  <section class="card card-logo-side">
    <span class="brand-dot-large"></span>
    <span class="brand-name-large">Vellum Crest</span>
  </section>

</main>
</body>
</html>
```